Guaranteed Job - Sleek Sexy Business Card UV Spot

Im looking for a sleek and sexy business card, that resembles elite or VIP status status.
our business is corinvale.example
you can view our products on there, but our main audience for handing out our cards will be for people in the hospitality industry, so it will need to impress high management and CEO of hotels and restaurants, bars, clubs etc...
the card features will have UV spot on both sides, 400gsm stock. standard size.
Artwork should be 86 x 54mm + 2mm bleed = 90 x 58mm
it should have a nice "unique" uv spot pattern that highlights the card, not a repeated pattern, theres no originality there, and it will be disregarded.
The written material will be:
Corin Vale Hospitality College (logo)
Tobin Marsh
Director
Phone: 1300 615 737
Mobile: 0455 817 296
Email: info@corinvale.example
website: www.corinvale.example
I'm looking for originality here, i don't want just a simple stock card, want something that has a wow factor for people.
You will find the logo attached. you may invert the white to black words to suit the background as you please.
thank you and good luck
As a side note, ive received a lot of proposals, im too busy to give feedback to each and every one, so if i havent provided feedback for your design within 24 hours, then consider it not acceptable, and you could resubmit another design.
So far i have not seen any design that stood out for me, they all seem pretty generic. there nothing thats unique, i would figure for the amount that im offering, that people would put some more effort and creativity into the design.
so far over 200 designs submitted, and nothing i have seen looks very original, everything looks like a different variation of the same stuff, i said it very clearly i wanted something unique, the only thing that has come close to it so far is this one
Reason: Ive received alot of design concepts and i have reviewed everyone, but i havent had time to give feedback to every single one, only the ones that have interested me, if i havent responded, its because i havent found it good enough.
so far only a few design have been on par with what ive been looking for, an attractive eye popping design.
heres a few of them,
http://files.pixelbazaar.example/design_img/51736/62418/62418_2840915_51736_image.jpg
http://files.pixelbazaar.example/design_img/51736/68254/68254_2841377_51736_image.jpg
theyre, both unique and original, and eye catching, the only thing theyre missing is the sexyness.
if you still think you have some creativity left in your minds, then throw it on here.
Reason: Sorry guys for the delay, I was in a serious accident and out of commission for the past few months, I'm just slowly recovering now, please bare with me as i try to attend to this project, it may take me awhile as I have other projects that are on standby, I'm not 100% at the moment, so im extending the deadline for 2 weeks right now. Thanks for your patience.
Hospitality

```html
<!DOCTYPE html>
<html lang="en">
<head>
<meta charset="utf-8">
<title>Corin Vale Hospitality College – Business Card</title>
<link href="https://fonts.googleapis.com/css2?family=Questrial&family=Great+Vibes&display=swap" rel="stylesheet">
<style>
  :root {
    --backdrop: #3a3a3c;
    --card-black: #050608;
    --card-navy: #070b1c;
    --accent-blue: #2b8fd8;
    --accent-dark: #0a1730;
    --text-light: #e9edf2;
    --text-muted: #b8c2cc;
    --splash-light: #9fb6cf;
    --splash-blue: #1d4f9a;
  }
  * { margin: 0; padding: 0; box-sizing: border-box; }
  html, body {
    width: 1200px; height: 900px; overflow: hidden;
    background: var(--backdrop);
    font-family: "Questrial", "Century Gothic", sans-serif;
  }
  .canvas { position: relative; width: 1200px; height: 900px; }

  .card {
    position: absolute;
    width: 560px; height: 352px;
    border-radius: 18px;
    overflow: hidden;
    background: var(--card-black);
    box-shadow: 0 14px 30px rgba(0,0,0,.45);
  }
  .card--front { left: 60px; top: 60px; background: var(--card-navy); }
  .card--back { left: 580px; top: 480px; }

  .splash {
    position: absolute;
    background:
      radial-gradient(ellipse 38% 34% at 62% 38%, rgba(190,210,230,.55), transparent 70%),
      radial-gradient(ellipse 70% 60% at 55% 45%, var(--splash-blue), transparent 75%);
  }
  .card--front .splash { left: 120px; top: 0; width: 440px; height: 300px; }
  .card--back .splash {
    left: 220px; top: 0; width: 340px; height: 240px;
    background:
      radial-gradient(ellipse 22% 22% at 30% 20%, rgba(170,195,225,.45), transparent 70%),
      radial-gradient(ellipse 30% 45% at 78% 55%, rgba(150,170,190,.35), transparent 70%),
      radial-gradient(ellipse 70% 50% at 50% 40%, rgba(20,45,90,.55), transparent 80%);
  }

  .brand {
    position: absolute;
    display: flex; align-items: center; gap: 10px;
    font-size: 14px; line-height: 1.15; letter-spacing: .4px;
    text-transform: uppercase;
    white-space: nowrap;
  }
  .brand__mark { width: 32px; height: 32px; flex: none; }
  .brand__name { display: flex; flex-direction: column; }

  .card--front .brand-band {
    position: absolute; left: 0; top: 220px;
    width: 250px; height: 62px;
    background: var(--accent-blue);
  }
  .card--front .brand { left: 14px; top: 235px; color: var(--accent-dark); }
  .card--front .brand__mark { background: var(--accent-dark); }
  .card--front .site-script {
    position: absolute; left: 70px; top: 290px;
    font-family: "Great Vibes", cursive;
    font-size: 20px; color: var(--accent-blue);
  }

  .card--back .brand { left: 50px; top: 66px; color: var(--text-light); font-size: 16px; }
  .card--back .brand__mark { width: 36px; height: 36px; background: var(--accent-blue); }

  .name-band {
    position: absolute; left: 32px; top: 180px;
    width: 196px; height: 50px;
    background: var(--accent-blue);
    padding: 6px 0 0 54px;
    color: var(--accent-dark);
    white-space: nowrap;
  }
  .name-band__name { font-size: 19px; line-height: 1.1; }
  .name-band__role { font-size: 13px; }

  .contacts { position: absolute; list-style: none; color: var(--text-light); font-size: 17px; letter-spacing: .5px; white-space: nowrap; }
  .contacts li { display: flex; align-items: center; gap: 16px; height: 26px; }
  .contacts svg { width: 14px; height: 14px; flex: none; }
  .contacts--phone { left: 110px; top: 258px; }
  .contacts--online { left: 330px; top: 194px; }
</style>
</head>
<body>
<main class="canvas">

  <section class="card card--front" aria-label="Card front">
    <div class="splash" role="img" aria-label="Photograph of a cocktail glass with water splashing out against a dark blue background"></div>
    <div class="brand-band"></div>
    <div class="brand">
      <span class="brand__mark"></span>
      <span class="brand__name"><span>Corin Vale</span><span>Hospitality College</span></span>
    </div>
    <p class="site-script">www.corinvale.example</p>
  </section>

  <section class="card card--back" aria-label="Card back">
    <div class="splash" role="img" aria-label="Photograph of a cocktail glass and water splashes fading into black"></div>
    <div class="brand">
      <span class="brand__mark"></span>
      <span class="brand__name"><span>Corin Vale</span><span>Hospitality College</span></span>
    </div>

    <div class="name-band">
      <p class="name-band__name">Tobin Marsh</p>
      <p class="name-band__role">Director</p>
    </div>

    <ul class="contacts contacts--phone">
      <li>
        <svg viewBox="0 0 14 14" aria-hidden="true"><circle cx="7" cy="7" r="6" fill="none" stroke="#2b8fd8" stroke-width="1.4"/><path d="M4.5 4.5c0 3 2 5 5 5l.6-1.4-1.5-.8-.7.7c-1-.4-1.6-1-2-2l.7-.7-.8-1.5z" fill="#2b8fd8"/></svg>
        <span>1300 615 737</span>
      </li>
      <li>
        <svg viewBox="0 0 14 14" aria-hidden="true"><rect x="4" y="1" width="6.5" height="12" rx="1.2" fill="none" stroke="#2b8fd8" stroke-width="1.4"/><circle cx="7.25" cy="10.8" r=".8" fill="#2b8fd8"/></svg>
        <span>0455 817 296</span>
      </li>
    </ul>

    <ul class="contacts contacts--online">
      <li>
        <svg viewBox="0 0 14 14" aria-hidden="true"><circle cx="7" cy="7" r="2.4" fill="none" stroke="#2b8fd8" stroke-width="1.4"/><path d="M9.4 5v3c0 1.6 2.8 1.6 2.8-1A5.2 5.2 0 1 0 9.5 11.6" fill="none" stroke="#2b8fd8" stroke-width="1.4"/></svg>
        <span>info@corinvale.example</span>
      </li>
      <li>
        <svg viewBox="0 0 14 14" aria-hidden="true"><path d="M1 7 7 1.5 13 7h-2v5.5H8.5V9h-3v3.5H3V7z" fill="#2b8fd8"/></svg>
        <span>www.corinvale.example</span>
      </li>
    </ul>
  </section>

</main>
</body>
</html>
```